New Product Design

We want to develop new Wafer Biscuits Product design of Vanilla / strawberry / choclate flavour. Designer can design first any of the flavour ( Vanilla/Chcolate/Starwberry). Based on the first any variety design will go for other designs.
Wafer is in finger form .
Name of the Brand will be ZOB ZIN
Wafer fingre (sample pics and ZOB ZIN brand image is attached in word file for reference.

Smaple pics of the fingre is attached for ref.

Target Market(s)

Children and Youth

Industry/Entity Type

Food

```html
<!DOCTYPE html>
<html lang="en">
<head>
<meta charset="utf-8">
<title>ZOB ZIN Wafer – Flavour Packs</title>
<link href="https://fonts.googleapis.com/css2?family=Open+Sans:wght@400;700;800&display=swap" rel="stylesheet">
<style>
  :root {
    --choc-dark: #1c0b03;
    --choc-mid: #5a2707;
    --choc-light: #7a3a0c;
    --choc-rule: #170802;
    --van-base: #e0c244;
    --van-light: #f0e0a2;
    --van-title: #a8390f;
    --van-title-low: #6b5a12;
    --straw-base: #f8286c;
    --straw-mid: #f76a96;
    --straw-light: #fda6c2;
    --fold-light: #ffffff;
    --wafer-gold: #f0c456;
    --wafer-deep: #d9a23a;
    --choc-fill: #6a3414;
    --cream-fill: #f3e2b6;
    --pink-fill: #f2b3b0;
    --white: #ffffff;
  }
  * { margin: 0; padding: 0; box-sizing: border-box; }
  html, body { width: 1196px; height: 1200px; overflow: hidden; background: #ffffff; }
  body { font-family: "Open Sans", Arial, sans-serif; }

  .pack { position: relative; width: 1196px; height: 400px; overflow: hidden; }
  .pack--chocolate { --rule: var(--choc-rule); background: radial-gradient(ellipse 62% 80% at 50% 60%, var(--choc-light), var(--choc-mid) 55%, var(--choc-dark)); }
  .pack--vanilla { --rule: var(--fold-light); background: radial-gradient(ellipse 45% 65% at 50% 72%, var(--van-light), var(--van-base) 75%); }
  .pack--strawberry { --rule: var(--fold-light); background: radial-gradient(ellipse 55% 75% at 50% 65%, var(--straw-light), var(--straw-mid) 55%, var(--straw-base)); }

  .rule { position: absolute; background: var(--rule); }
  .rule--v { top: 0; bottom: 0; width: 2px; }
  .rule--h { left: 0; right: 0; height: 2px; }

  .brand { position: absolute; color: var(--white); font-weight: 800; line-height: 0.95; letter-spacing: 1px; }
  .brand--main { left: 192px; top: 34px; font-size: 74px; }
  .brand--small { left: 200px; top: 312px; font-size: 29px; }
  .brand__descriptor { position: absolute; left: 296px; top: 170px; font-size: 34px; font-weight: 400; color: var(--white); }
  .pack--vanilla .brand__descriptor { color: #2a1a08; }
  .pack--strawberry .brand__descriptor { color: #3a1018; }

  .flavour { position: absolute; color: var(--white); white-space: nowrap; }
  .flavour__name { font-weight: 700; font-size: 19px; line-height: 23px; }
  .flavour__type { font-weight: 400; font-size: 14.5px; line-height: 20px; word-spacing: 3px; }
  .flavour--front { left: 815px; top: 40px; }
  .flavour--side { left: 312px; top: 321px; }
  .pack--vanilla .flavour--front,
  .pack--strawberry .flavour--front { left: 838px; }
  .pack--vanilla .flavour--front { color: var(--van-title); }
  .pack--vanilla .flavour--side { color: var(--van-title-low); }

  .net-weight { position: absolute; left: 689px; top: 357px; font-weight: 700; font-size: 20px; color: var(--white); }
  .pack--vanilla .net-weight { color: var(--van-title-low); }

  .wafer-visual { position: absolute; border-radius: 10px; }
  .wafer-visual--hero { left: 424px; top: 44px; width: 382px; height: 200px; }
  .wafer-visual--mini { left: 843px; top: 298px; width: 163px; height: 86px; border-radius: 6px; }
  .pack--vanilla .wafer-visual--hero,
  .pack--strawberry .wafer-visual--hero { left: 412px; top: 44px; width: 394px; height: 206px; }
  .pack--chocolate .wafer-visual { background: linear-gradient(180deg, var(--wafer-gold) 10%, var(--wafer-deep) 55%, var(--choc-fill)); }
  .pack--vanilla .wafer-visual { background: linear-gradient(180deg, var(--wafer-gold) 10%, var(--wafer-deep) 55%, var(--cream-fill)); }
  .pack--strawberry .wafer-visual { background: linear-gradient(180deg, var(--wafer-gold) 10%, var(--wafer-deep) 55%, var(--pink-fill)); }
</style>
</head>
<body>

<section class="pack pack--chocolate">
  <div class="rule rule--v" style="left:93px"></div>
  <div class="rule rule--v" style="left:153px"></div>
  <div class="rule rule--v" style="left:1043px"></div>
  <div class="rule rule--v" style="left:1106px"></div>
  <div class="rule rule--h" style="top:260px"></div>
  <div class="rule rule--h" style="top:288px"></div>
  <div class="brand brand--main">ZOB<br>ZIN</div>
  <div class="brand__descriptor">wafer</div>
  <div class="wafer-visual wafer-visual--hero" role="img" aria-label="Layered wafer with melting chocolate filling"></div>
  <div class="flavour flavour--front"><p class="flavour__name">MELTING CHOCOLATE</p><p class="flavour__type">FLAVOUR FILLED WAFER</p></div>
  <div class="brand brand--small">ZOB<br>ZIN</div>
  <div class="flavour flavour--side"><p class="flavour__name">MELTING CHOCOLATE</p><p class="flavour__type">FLAVOUR FILLED WAFER</p></div>
  <div class="net-weight">NET WT 35G</div>
  <div class="wafer-visual wafer-visual--mini" role="img" aria-label="Small chocolate filled wafer"></div>
</section>

<section class="pack pack--vanilla">
  <div class="rule rule--v" style="left:93px"></div>
  <div class="rule rule--v" style="left:153px"></div>
  <div class="rule rule--v" style="left:1039px"></div>
  <div class="rule rule--v" style="left:1101px"></div>
  <div class="rule rule--h" style="top:257px"></div>
  <div class="rule rule--h" style="top:285px"></div>
  <div class="brand brand--main">ZOB<br>ZIN</div>
  <div class="brand__descriptor">wafer</div>
  <div class="wafer-visual wafer-visual--hero" role="img" aria-label="Layered wafer with melting vanilla cream filling"></div>
  <div class="flavour flavour--front"><p class="flavour__name">MELTING VENILLA</p><p class="flavour__type">FLAVOUR FILLED WAFER</p></div>
  <div class="brand brand--small">ZOB<br>ZIN</div>
  <div class="flavour flavour--side"><p class="flavour__name">MELTING VANNILA</p><p class="flavour__type">FLAVOUR FILLED WAFER</p></div>
  <div class="net-weight">NET WT 35G</div>
  <div class="wafer-visual wafer-visual--mini" role="img" aria-label="Small vanilla filled wafer"></div>
</section>

<section class="pack pack--strawberry">
  <div class="rule rule--v" style="left:93px"></div>
  <div class="rule rule--v" style="left:153px"></div>
  <div class="rule rule--v" style="left:1041px"></div>
  <div class="rule rule--v" style="left:1103px"></div>
  <div class="rule rule--h" style="top:258px"></div>
  <div class="rule rule--h" style="top:286px"></div>
  <div class="brand brand--main">ZOB<br>ZIN</div>
  <div class="brand__descriptor">wafer</div>
  <div class="wafer-visual wafer-visual--hero" role="img" aria-label="Layered wafer with melting strawberry cream filling"></div>
  <div class="flavour flavour--front"><p class="flavour__name">MELTING STROBERY</p><p class="flavour__type">FLAVOUR FILLED WAFER</p></div>
  <div class="brand brand--small">ZOB<br>ZIN</div>
  <div class="flavour flavour--side"><p class="flavour__name">MELTING STROBERY</p><p class="flavour__type">FLAVOUR FILLED WAFER</p></div>
  <div class="net-weight">NET WT 35G</div>
  <div class="wafer-visual wafer-visual--mini" role="img" aria-label="Small strawberry filled wafer"></div>
</section>

</body>
</html>
```